Design some Business Cards

Note: Designs submitted so far are too heavy. Too much bright red color. I would like to restate that I want a white business card with minimal use of red/green or any other color.

I want to create a business card for a financial advisory. Name of the company is "TelvanQuo Capital Partners". The company advises clients on investments in global equity and real estate markets.

I want a CLEAN and MINIMALIST design. I want a white business card with a tinge of red. Don't want a coloured card.

An example of front side of the business card I have with me. Please see attached file BC1. I also need a design for the back side of the business card.
These are only examples. No need to mimic these. I am open to all designs.

Details I want on the business card as follows:

Name: Deven K. Mahajan

Designation: Advisor

Address: 617, Ashvale Nook Co-operative Society,
Opposite Kirana Plaza, Lake Lane, Vashi, 400703.

Tel: (+91) 98213 57420

Website: [url removed, login to view]

Email: [url removed, login to view]@[url removed, login to view]

I want to add the following comparison of "What We Do" and "What We Don't Do" (i.e. what our competition does.)
So basically on the business card itself, I want these differences highlighted.

Here's the text:

What We Do | What We Don't Do
|
Prudent Advise | Salesy Pitches
Build Your Portfolio | Sell You Products
Focused, Principled Investing | Double-your-money-guaranteed
Comprehensive Planning | Short-term Trading

Please attached examples that I found for Dos and Don'ts. These are just examples. No need to mimic these. I am OPEN TO ALL IDEAS.

I am also attaching the logo files.

The style has to be highly professional, sophisticated and slick.
I would describe the requirement as below:

1. Trustworthy - People give us their savings to manage. Trust is essential.
2. Elegant / classy - This is a top investment management company.
3. Clean

```html
<!DOCTYPE html>
<html lang="en">
<head>
<meta charset="utf-8">
<title>TelvanQuo Capital Partners – Business Card</title>
<link href="https://fonts.googleapis.com/css2?family=Lato:wght@400;700&display=swap" rel="stylesheet">
<style>
  :root {
    --bg: #e4e1dd;
    --card: #ffffff;
    --ink: #2b2b2b;
    --ink-soft: #3c3c3c;
    --accent: #e8231f;
    --rule: #ef8a86;
    --divider: #555555;
  }
  * { box-sizing: border-box; margin: 0; padding: 0; }
  html, body { width: 1200px; height: 1200px; overflow: hidden; }
  body {
    position: relative;
    background: var(--bg);
    font-family: "Lato", sans-serif;
    color: var(--ink);
  }
  .card {
    position: absolute;
    left: 180px;
    width: 840px;
    background: var(--card);
    border-radius: 40px;
    box-shadow: 0 6px 22px rgba(0,0,0,0.12);
  }
  .card--front { top: 56px; height: 477px; }
  .card--back { top: 577px; height: 480px; }

  /* Front */
  .brand {
    position: absolute;
    left: 70px;
    top: 190px;
    width: 300px;
    display: flex;
    align-items: center;
    gap: 14px;
  }
  .brand__dot {
    flex: 0 0 auto;
    width: 18px; height: 18px;
    border-radius: 50%;
    background: var(--accent);
  }
  .brand__name {
    font-weight: 700;
    font-size: 30px;
    line-height: 1.15;
    color: var(--ink);
  }
  .person { position: absolute; left: 411px; top: 122px; width: 380px; }
  .person__name { font-size: 37px; font-weight: 700; line-height: 1.1; color: var(--ink); white-space: nowrap; }
  .person__first { color: var(--accent); }
  .person__role { font-size: 18px; margin-top: 4px; color: var(--ink-soft); }
  .rule { height: 1.5px; background: var(--rule); width: 326px; }
  .rule--top { margin-top: 14px; }
  .rule--mid { margin-top: 12px; }
  .contacts { list-style: none; margin-top: 8px; }
  .contacts li {
    display: flex; align-items: center; gap: 10px;
    font-size: 19px; line-height: 28px; color: var(--ink-soft); white-space: nowrap;
  }
  .contacts svg { width: 16px; height: 16px; flex: 0 0 auto; }
  .address {
    font-size: 19px; line-height: 27px; margin-top: 9px;
    color: var(--ink-soft); font-style: normal; white-space: nowrap;
  }

  /* Back */
  .back-brand {
    position: absolute; top: 95px; left: 0; width: 100%;
    text-align: center; font-weight: 700; font-size: 32px; color: var(--ink);
  }
  .compare { position: absolute; top: 200px; left: 0; width: 100%; }
  .compare__col { position: absolute; top: 0; }
  .compare__col--dont { right: 440px; text-align: right; }
  .compare__col--do { left: 444px; }
  .compare__heading { font-size: 22px; font-weight: 700; color: var(--ink-soft); margin-bottom: 6px; white-space: nowrap; }
  .compare__list { list-style: none; }
  .compare__list li {
    display: flex; align-items: center; gap: 10px;
    font-size: 21px; line-height: 33.5px; color: var(--ink-soft); white-space: nowrap;
  }
  .compare__col--dont .compare__list li { justify-content: flex-end; }
  .compare__list svg { width: 14px; height: 14px; flex: 0 0 auto; }
  .compare__divider {
    position: absolute; left: 423px; top: 3px;
    width: 2px; height: 153px; background: var(--divider);
  }
  .back-url {
    position: absolute; top: 400px; left: 0; width: 100%;
    text-align: center; font-size: 20px; letter-spacing: 1.5px; color: var(--ink-soft);
  }
</style>
</head>
<body>

<section class="card card--front">
  <div class="brand">
    <span class="brand__dot"></span>
    <span class="brand__name">TelvanQuo<br>Capital Partners</span>
  </div>

  <div class="person">
    <h1 class="person__name"><span class="person__first">Deven</span> K. Mahajan</h1>
    <p class="person__role">Advisor</p>
    <div class="rule rule--top"></div>
    <ul class="contacts">
      <li>
        <svg viewBox="0 0 16 16"><path fill="#e8231f" d="M3.5 1.5l2.5 0 1 3.5-1.7 1.2c.8 1.8 2.2 3.2 4 4l1.2-1.7 3.5 1v2.5c0 .8-.7 1.5-1.5 1.5C6.7 13.5 2.5 9.3 2 3c0-.8.7-1.5 1.5-1.5z"/></svg>
        (+91) 98213 57420
      </li>
      <li>
        <svg viewBox="0 0 16 16"><rect x="1.5" y="3.5" width="13" height="9" rx="1" fill="#e8231f"/><path d="M2 4.5l6 4.5 6-4.5" fill="none" stroke="#fff" stroke-width="1.4"/></svg>
        advisors@telvanquo.com
      </li>
      <li>
        <svg viewBox="0 0 16 16"><circle cx="8" cy="8" r="6.5" fill="#e8231f"/><path d="M1.5 8h13M8 1.5c2 2 2 11 0 13M8 1.5c-2 2-2 11 0 13" fill="none" stroke="#fff" stroke-width="1.1"/></svg>
        www.telvanquo.com
      </li>
    </ul>
    <div class="rule rule--mid"></div>
    <address class="address">
      617, Ashvale Nook Co-operative Society<br>
      Opposite Kirana Plaza, Lake Lane<br>
      Vashi, 400703
    </address>
  </div>
</section>

<section class="card card--back">
  <div class="back-brand">TelvanQuo Capital Partners</div>

  <div class="compare">
    <div class="compare__col compare__col--dont">
      <h2 class="compare__heading">WHAT WE DON'T DO</h2>
      <ul class="compare__list">
        <li>Salesy Pitches <svg viewBox="0 0 14 14"><circle cx="7" cy="7" r="5.5" fill="none" stroke="#2b2b2b" stroke-width="1.8"/><path d="M3.2 10.8l7.6-7.6" stroke="#2b2b2b" stroke-width="1.8"/></svg></li>
        <li>Sell You Products <svg viewBox="0 0 14 14"><circle cx="7" cy="7" r="5.5" fill="none" stroke="#2b2b2b" stroke-width="1.8"/><path d="M3.2 10.8l7.6-7.6" stroke="#2b2b2b" stroke-width="1.8"/></svg></li>
        <li>Double-your-money-guaranteed <svg viewBox="0 0 14 14"><circle cx="7" cy="7" r="5.5" fill="none" stroke="#2b2b2b" stroke-width="1.8"/><path d="M3.2 10.8l7.6-7.6" stroke="#2b2b2b" stroke-width="1.8"/></svg></li>
        <li>Short-term Trading <svg viewBox="0 0 14 14"><circle cx="7" cy="7" r="5.5" fill="none" stroke="#2b2b2b" stroke-width="1.8"/><path d="M3.2 10.8l7.6-7.6" stroke="#2b2b2b" stroke-width="1.8"/></svg></li>
      </ul>
    </div>

    <div class="compare__divider"></div>

    <div class="compare__col compare__col--do">
      <h2 class="compare__heading">WHAT WE DO</h2>
      <ul class="compare__list">
        <li><svg viewBox="0 0 14 14"><circle cx="7" cy="7" r="6" fill="#2b2b2b"/><path d="M4 7.2l2 2 4-4" fill="none" stroke="#fff" stroke-width="1.5"/></svg> Prudent Advise</li>
        <li><svg viewBox="0 0 14 14"><circle cx="7" cy="7" r="6" fill="#2b2b2b"/><path d="M4 7.2l2 2 4-4" fill="none" stroke="#fff" stroke-width="1.5"/></svg> Build Your Portfolio</li>
        <li><svg viewBox="0 0 14 14"><circle cx="7" cy="7" r="6" fill="#2b2b2b"/><path d="M4 7.2l2 2 4-4" fill="none" stroke="#fff" stroke-width="1.5"/></svg> Focused, Principled Investing</li>
        <li><svg viewBox="0 0 14 14"><circle cx="7" cy="7" r="6" fill="#2b2b2b"/><path d="M4 7.2l2 2 4-4" fill="none" stroke="#fff" stroke-width="1.5"/></svg> Comprehensive Planning</li>
      </ul>
    </div>
  </div>

  <div class="back-url">www.telvanquo.com</div>
</section>

</body>
</html>
```